GLIMMER Print Shop

We need postcards for a new print shop in Newark Delaware called GLIMMER. We specialize in screen printing however the fun doesn't stop there...we also provide services for many other promotional product such as; embroidery, decals/ stickers, banners, yard signs, and sublimation products. We deal with customers from all walks of life; businesses, sporting events, bands, bars/restaurants, schools/ colleges. Our main goal is to have our customers look awesome in that custom shirt, hat, or any other custom product that we make because let’s face it first impressions are everything! At GLIMMER we strive to create a lasting experience every step of the way to ensure complete satisfaction and trust in our products. The colors we use to identify ourselves are neon green and turquoise. The slogan we want to run with is, "we bring your ideas to life". On the back we would like to add a 10% off next order coupon to generate new revenue.
Color Breakdown in logo:
Green- R=0, G=255, B=0
blue- R=0, G=118, B=163
Reason: times running out we still need a design!!
Target Market(s)
everybody & anybody
Industry/Entity Type
Promotional Product
Requirements
Must have
- website: www.glimmerinkworks-example.com
contact info: (302)555-0147 & glimmerpw@mailbox-example.com
like us on FB: www.socialsite-example.com/glimmerinkshop
Nice to have
- stack of t-shirts

```html
<!DOCTYPE html>
<html lang="en">
<head>
<meta charset="utf-8">
<title>GLIMMER Print Shop – Postcard Back</title>
<link rel="stylesheet" href="https://fonts.googleapis.com/css2?family=Amatic+SC:wght@700&family=Jost:wght@400&family=Tinos&display=swap">
<style>
  :root {
    --paper: #ffffff;
    --ink-dark: #262223;
    --turquoise: #0076a3;
    --band: #0a7b9f;
    --neon-green: #00ff00;
    --white: #ffffff;
    --sky-top: #b9b8c4;
    --sky-mid: #e3e1d3;
    --sky-bottom: #ece5c9;
  }
  * { margin: 0; padding: 0; box-sizing: border-box; }
  html, body {
    width: 1200px;
    height: 900px;
    overflow: hidden;
    background: var(--paper);
  }
  .postcard {
    position: absolute;
    left: 120px;
    top: 78px;
    width: 962px;
    height: 740px;
  }
  .coupon-panel {
    position: absolute;
    left: 0;
    top: 0;
    width: 463px;
    height: 610px;
    display: block;
  }
  .coupon-headline {
    font-family: "Amatic SC", "Arial Narrow", sans-serif;
    font-weight: 700;
    fill: var(--white);
  }
  .coupon-terms {
    font-family: "Jost", "Futura", sans-serif;
    font-weight: 400;
    fill: var(--white);
  }
  .brand-name {
    font-family: "Amatic SC", "Arial Narrow", sans-serif;
    font-weight: 700;
    fill: var(--turquoise);
  }
  .mailing-area {
    position: absolute;
    left: 463px;
    top: 0;
    width: 499px;
    height: 610px;
    background: var(--ink-dark);
    color: var(--white);
    font-family: "Tinos", "Times New Roman", serif;
    font-size: 76px;
    line-height: 95px;
    text-align: center;
    padding-top: 160px;
    letter-spacing: 1px;
  }
  .barcode-area {
    position: absolute;
    left: 0;
    top: 610px;
    width: 962px;
    height: 130px;
    background: var(--ink-dark);
    color: var(--white);
    font-family: "Tinos", "Times New Roman", serif;
    font-size: 92px;
    line-height: 130px;
    text-align: center;
    letter-spacing: 2px;
  }
</style>
</head>
<body>
  <main class="postcard">
    <svg class="coupon-panel" viewBox="0 0 463 610" width="463" height="610" xmlns="http://www.w3.org/2000/svg">
      <defs>
        <linearGradient id="sky-wash" x1="0" y1="0" x2="0" y2="1">
          <stop offset="0" stop-color="var(--sky-top)"/>
          <stop offset="0.5" stop-color="var(--sky-mid)"/>
          <stop offset="1" stop-color="var(--sky-bottom)"/>
        </linearGradient>
      </defs>

      <rect class="coupon-backdrop" x="0" y="0" width="463" height="610" fill="url(#sky-wash)" role="img" aria-label="Soft hazy sky photograph behind the coupon"/>

      <g class="coupon-band">
        <polygon points="0,50 463,-12 463,284 0,354" fill="var(--band)"/>
        <line x1="0" y1="42" x2="463" y2="-2" stroke="var(--white)" stroke-width="2" stroke-dasharray="12 8"/>
        <line x1="0" y1="332" x2="463" y2="266" stroke="var(--white)" stroke-width="2" stroke-dasharray="12 8"/>

        <g transform="rotate(-7 230 200)">
          <text class="coupon-headline" x="222" y="158" font-size="150" text-anchor="middle" textLength="318" lengthAdjust="spacingAndGlyphs">10% OFF</text>
          <text class="coupon-headline" x="240" y="250" font-size="80" text-anchor="middle" textLength="384" lengthAdjust="spacingAndGlyphs">YOUR NEXT PURCHASE</text>
          <text class="coupon-terms" x="246" y="290" font-size="15" text-anchor="middle" textLength="300" lengthAdjust="spacingAndGlyphs">Offer expires 6/30/14. One coupon per client</text>
        </g>
      </g>

      <g class="brand-lockup">
        <text class="brand-name" x="225" y="488" font-size="140" text-anchor="middle" textLength="360" lengthAdjust="spacingAndGlyphs">GLIMMER</text>
        <circle cx="98" cy="534" r="28" fill="var(--neon-green)"/>
      </g>
    </svg>

    <section class="mailing-area">ADDRESS<br>&amp;<br>POSTCARD<br>AREA</section>
    <section class="barcode-area">BARCODE AREA</section>
  </main>
</body>
</html>
```